Velbrook Leaf is a bridge for the people who drink tea to connect with the people who make the tea and the environment in which it is grown.

As a start-up, Velbrook Leaf needs to establish a fluently persuasive brand image that articulates its unique mission to the up-market tea drinker.

Our passion for high quality tea and our respect for people are boundless. But our budget is shoe-string. Still, we will allocate a disproportionate amount to evolving a brand; including logo, labeling, and packaging, and hope this initial effort will lead to a long-term relationship with a designer. The Velbrook label, as a component of the brand, must deny the commodity image of tea by broadcasting the uniquely flavorful, healthful, and relaxing experience of drinking tea.

The logo is an image of a liquor pouring from above into a stylized outline of a cup and gracefully folding over on itself within the cup. The image is an echo of video clips that will be featured on the Product page of the ecommerce site. Our initial thought is for the liquor and cup to be white on a rich blue background. But you may have a better idea.

The label must fit a seamless tin canister 4" in diameter; 2" high with a "window" in the lid. There are really three distinct parts to the label: a) wrap-around for the body of the tin; b) a distinct piece to be applied underneath the tin; and c) security strip (s) that connect the lid and the bottom of the tin. The wrap-around must include the following components: the logo, the brand name 'Velbrook Leaf', the name of the specific tea and space for the following characteristics of the tea: Tea / Garden Name, Harvest Date, Tasting Notes, Weight, Location, and Caffeine content. The piece to be affixed underneath the tin should accommodate Ingredients, Brewing Instructions, and contact details for Velbrook Leaf. The security strip(s) should be an integral part of the overall visual.

The color scheme should be expandable, i.e.; different colors for different teas.
We are thinking about rich and bold colors. But am eager to see what inspires you!

A very rough proto-type is captured in the attached files.

Target Market(s)

Ages 25 to 45 in densely populated areas of the U.S. and Canada will an above average house-hold income and an interest in what they eat / drink.

Industry/Entity Type

Environment

Requirements
Must have
• 1. Three separate pieces: 1) wrap around for the body of the tin; 2) piece to be affixed to the bottom of the body of the tin; 3) security strip (s). A word about strips: am unsure about one vs two because, two will add to overhead and processing while one will block the view of the contents. Maybe you know how to resolve.
2. clean, crisp lines
3. uncluttered
Nice to have
• 1. a color scheme to accommodate up to 30 different teas. Do not fall into the trap of incorporating the color green on the label for a 'green tea' and yellow for a lemon flavored tea. That approach is limited and has been overdone.
2. a color scheme that, as it expands to accommodate 30 teas, also is anchored by a brand color set. In other words, all labels include a recognizable color set.
3. express the level of caffeine via a gauge or metric
Should not have
• photo images,

```html
<!DOCTYPE html>
<html lang="en">
<head>
<meta charset="utf-8">
<title>Velbrook Leaf – Base Label</title>
<link rel="stylesheet" href="https://fonts.googleapis.com/css2?family=Arimo:wght@700&family=Questrial&display=swap">
<style>
  :root {
    --canvas: #ffffff;
    --brand-blue: #2f3bff;
    --label-pink: #f7d3e6;
    --accent-magenta: #ff1a72;
    --wordmark-white: #ffffff;
  }
  html, body {
    margin: 0;
    padding: 0;
    width: 1200px;
    height: 932px;
    overflow: hidden;
    background: var(--canvas);
  }
  .base-label {
    position: relative;
    width: 1200px;
    height: 932px;
    font-family: "Questrial", "Century Gothic", sans-serif;
  }
  .label-disc {
    position: absolute;
    left: 0;
    top: 0;
  }
  .label-text {
    position: absolute;
    margin: 0;
    line-height: 1;
    white-space: nowrap;
  }
  .section-heading {
    font-family: "Arimo", Arial, sans-serif;
    font-weight: 700;
    font-size: 37px;
    color: var(--label-pink);
  }
  .brewing-heading {
    left: 113px;
    top: 140px;
    width: 300px;
    text-align: center;
    line-height: 56px;
  }
  .ingredients-heading {
    left: 465px;
    top: 140px;
    line-height: 40px;
  }
  .brewing-copy {
    font-size: 40px;
    color: var(--label-pink);
    letter-spacing: -0.5px;
  }
  .brewing-copy span {
    position: absolute;
    white-space: nowrap;
  }
  .ingredient-list {
    position: absolute;
    left: 463px;
    top: 246px;
    margin: 0;
    padding: 0;
    list-style: none;
    font-size: 40px;
    color: var(--label-pink);
    letter-spacing: -0.5px;
  }
  .ingredient-list li {
    height: 58.5px;
    line-height: 46px;
  }
  .ingredient-list .bullet {
    font-size: 26px;
    vertical-align: 4px;
    margin-right: 1px;
  }
  .best-before {
    left: 0;
    width: 966px;
    text-align: center;
    top: 617px;
    font-size: 36px;
    color: var(--accent-magenta);
    letter-spacing: -0.3px;
  }
  .brand-name {
    left: 0;
    width: 906px;
    text-align: center;
    top: 733px;
    font-size: 42px;
    color: var(--wordmark-white);
  }
  .brand-url {
    left: 0;
    width: 906px;
    text-align: center;
    top: 790px;
    font-size: 31px;
    color: var(--wordmark-white);
  }
</style>
</head>
<body>
<main class="base-label">
  <svg class="label-disc" width="904" height="904" viewBox="0 0 904 904" aria-hidden="true">
    <circle cx="451" cy="451" r="449" fill="var(--brand-blue)"/>
  </svg>

  <h2 class="label-text section-heading brewing-heading">BREWING<br>INSTRUCTIONS</h2>
  <h2 class="label-text section-heading ingredients-heading">INGREDIENTS</h2>

  <p class="label-text brewing-copy">
    <span style="left:48px; top:304px;">Please follow these</span>
    <span style="left:30px; top:359px;">instructions for</span>
    <span style="left:18px; top:414px;">brewing tea. These</span>
    <span style="left:18px; top:469px;">instructions must be</span>
    <span style="left:28px; top:524px;">strictly followed.</span>
  </p>

  <ul class="ingredient-list">
    <li><span class="bullet">+</span>Caffeine</li>
    <li><span class="bullet">+</span>Calories</li>
    <li><span class="bullet">+</span>Flavours</li>
    <li><span class="bullet">+</span>Natural Colours</li>
    <li><span class="bullet">+</span>Preservatives</li>
  </ul>

  <p class="label-text best-before">Best Before 24 months of Packing</p>

  <p class="label-text brand-name">THE VELBROOK LEAF</p>
  <p class="label-text brand-url">www.velbrookleaf.com</p>
</main>
</body>
</html>
```